Therapy Dog Organization Website

Looking for a website that is user friendly, welcoming, dog themed and has the following pages and links:
*Click here to join - links to a jot form
*Click here to donate - links to our paypal page
*Request a visit - links to a jot form
*Facebook Follow Link
*Instagram Follow Link
*Our team - images uploaded to showcase our dogs
*Donors and Referrals Page - Where I can update as donations and referrals come in.
*Online store. Currently this is in Jot Form but I would like a store front. I would not want this to be a link but rather a hidden page, something like www.brightmeadow.org/teamstore.

Please visit www.brightmeadow.org to see what we have right now designed simply in Canva. Dog photos can be provided to use in images.

Note: I have funds from a grant that I have to spend to add gratuity to the project winner.

```html
<!DOCTYPE html>
<html lang="en">
<head>
<meta charset="utf-8">
<title>Bright Meadow Team Store</title>
<link href="https://fonts.googleapis.com/css2?family=Inter:wght@400;500;600;700&family=Playfair+Display:wght@600;700&display=swap" rel="stylesheet">
<style>
:root{
  --navy:#1b3a4b;
  --navy-dark:#14283a;
  --orange:#d4896a;
  --orange-bright:#e8822e;
  --cream:#f5f1ec;
  --white:#ffffff;
  --text:#3a3f44;
  --muted:#5b6066;
  --green:#5f8f7a;
}
*{box-sizing:border-box;margin:0;padding:0}
html,body{width:1200px;height:2352px;overflow:hidden}
body{background:var(--cream);font-family:'Inter',sans-serif;color:var(--text);position:relative}
.site-header{height:82px;background:var(--white);display:flex;align-items:center;padding:0 88px;position:relative}
.brand{display:flex;align-items:center;gap:14px}
.brand-name{font-family:'Inter',sans-serif;font-weight:700;font-size:20px;color:var(--orange-bright);line-height:1.05}
.badge{width:40px;height:40px;border-radius:50%;background:#e7c74a}
.main-nav{position:absolute;left:460px;top:23px;display:flex;gap:8px}
.main-nav a{font-size:13.5px;font-weight:500;color:var(--navy);text-decoration:none;padding:0 16px;height:35px;display:flex;align-items:center;border-radius:18px}
.main-nav a.active{background:var(--navy);color:var(--white);font-weight:600}
.social{position:absolute;right:88px;top:22px;display:flex;gap:8px}
.social span{width:36px;height:36px;border-radius:50%;background:#e6e6e6;display:block}
.social span+span{background:#f0ebe5}
.hero{height:207px;background:linear-gradient(120deg,#1d4258,#15293b);text-align:center;color:var(--white);padding-top:56px}
.hero h1{font-family:'Playfair Display',serif;font-size:42px;font-weight:700;display:flex;justify-content:center;align-items:center;gap:20px;line-height:1}
.hero .lead{font-size:16.5px;margin-top:14px}
.hero .note{font-size:14px;color:#d6dde3;margin-top:12px}
.filters{display:flex;justify-content:center;gap:12px;margin-top:52px}
.filters span{height:36px;padding:0 23px;border-radius:18px;background:var(--white);border:2px solid #e5ded6;font-size:13px;font-weight:500;color:var(--navy);display:flex;align-items:center}
.filters span.active{background:var(--navy);border-color:var(--navy);color:var(--white);font-weight:600}
.products{display:grid;grid-template-columns:repeat(3,323px);column-gap:28px;grid-template-rows:421px 362px 362px;row-gap:30px;margin:39px 88px 0}
.card{background:var(--white);border-radius:22px;overflow:hidden;display:flex;flex-direction:column;box-shadow:0 4px 16px rgba(27,58,75,.06)}
.photo{height:178px;position:relative;flex:none}
.tag{position:absolute;left:13px;top:13px;background:var(--green);color:var(--white);font-size:10.5px;font-weight:700;padding:5px 12px;border-radius:12px}
.card-body{padding:18px 20px 21px;display:flex;flex-direction:column;flex:1}
.card-body h3{font-family:'Playfair Display',serif;font-size:17px;font-weight:700;color:var(--navy)}
.card-body p{font-size:12.8px;color:var(--muted);margin-top:6px;line-height:1.5}
.size{display:flex;align-items:center;gap:10px;font-size:12px;color:var(--navy);font-weight:500;margin-top:14px}
.size span.select{width:64px;height:28px;border:1.5px solid #d8d8d8;border-radius:6px;display:flex;align-items:center;justify-content:space-between;padding:0 8px 0 12px;color:#222;font-size:12.5px;font-weight:400}
.price{font-family:'Playfair Display',serif;font-size:24px;color:var(--orange);font-weight:600;margin-top:auto}
.add{margin-top:12px;height:39px;border-radius:20px;background:var(--orange);color:var(--white);font-size:14.5px;font-weight:600;display:flex;align-items:center;justify-content:center;gap:9px}
.cart-bar{margin:37px 88px 0;height:76px;background:var(--white);border-radius:20px;display:flex;align-items:center;justify-content:center;gap:16px}
.cart-icon{position:relative;margin-right:10px}
.cart-count{position:absolute;right:-10px;top:-10px;width:18px;height:18px;border-radius:50%;background:var(--orange-bright);color:var(--white);font-size:10px;font-weight:700;display:flex;align-items:center;justify-content:center}
.total{font-size:15px;font-weight:600;color:var(--navy)}
.total-amount{font-family:'Playfair Display',serif;font-size:23px;color:var(--orange);margin-right:16px}
.checkout{height:39px;padding:0 28px;border-radius:20px;background:var(--navy);color:var(--white);font-size:14.5px;font-weight:600;display:flex;align-items:center;gap:9px}
.bulk{margin:38px 88px 0;height:207px;background:var(--white);border-radius:22px;text-align:center;padding-top:42px}
.bulk h2{font-family:'Playfair Display',serif;font-size:28px;color:var(--navy);font-weight:700}
.bulk p{font-size:14.5px;margin-top:8px}
.bulk .contact{display:inline-flex;align-items:center;gap:9px;height:39px;padding:0 29px;border-radius:20px;background:var(--orange);color:var(--white);font-size:14.5px;font-weight:600;margin-top:22px}
.site-footer{position:absolute;left:0;top:2029px;width:1200px;height:323px;background:var(--navy-dark);color:#c4ccd3}
.foot-brand{position:absolute;left:88px;top:56px}
.foot-brand .brand-name{color:var(--white)}
.foot-brand p{font-size:14px;line-height:1.7;width:290px;margin-top:16px}
.foot-social{display:flex;gap:10px;margin-top:18px}
.foot-social span{width:37px;height:37px;border-radius:50%;background:#23394b;display:block}
.foot-col{position:absolute;top:60px}
.foot-col h4{font-size:15.5px;font-weight:700;color:var(--white);margin-bottom:16px}
.foot-col li{list-style:none;font-size:13.5px;margin-bottom:14px;display:flex;align-items:center;gap:12px}
.copyright{position:absolute;left:88px;right:88px;top:263px;border-top:1px solid #23394b;text-align:center;font-size:12.5px;color:#8b98a3;padding-top:25px}
</style>
</head>
<body>
<header class="site-header">
  <div class="brand">
    <div class="brand-name">Bright Meadow<br>Therapy Dogs</div>
    <span class="badge" role="img" aria-label="Certification badge"></span>
  </div>
  <nav class="main-nav">
    <a>Home</a><a>Our Team</a><a>Donors &amp; Referrals</a><a class="active">Store</a>
  </nav>
  <div class="social"><span role="img" aria-label="Social media link"></span><span role="img" aria-label="Photo sharing link"></span></div>
</header>

<section class="hero">
  <h1><svg width="44" height="40" viewBox="0 0 44 40"><path d="M4 4h36l4 10c0 4-3 6-6 6s-6-2-6-6c0 4-3 6-6 6s-6-2-6-6c0 4-3 6-6 6s-6-2-6-6c0 4-3 6-6 6S0 18 0 14z" fill="#e9a888"/><rect x="4" y="22" width="36" height="16" rx="3" fill="#e9a888"/><rect x="12" y="26" width="20" height="8" rx="1" fill="#1d4258"/></svg>Bright Meadow Team Store</h1>
  <p class="lead">Show your support with official Bright Meadow merchandise</p>
  <p class="note">All proceeds support our therapy dog programs</p>
</section>

<div class="filters"><span class="active">All Items</span><span>Apparel</span><span>Accessories</span><span>Stickers &amp; More</span></div>

<main class="products">
  <article class="card">
    <div class="photo" role="img" aria-label="Volunteer in navy t-shirt with a golden retriever" style="background:linear-gradient(135deg,#c9a47a,#2f3f6b 60%,#b88a55)"><span class="tag">Best Seller</span></div>
    <div class="card-body"><h3>Bright Meadow Classic T-Shirt</h3><p>Soft cotton blend with our iconic paw print logo</p>
      <div class="size">Size: <span class="select">S <svg width="8" height="5"><path d="M0 0l4 5 4-5" fill="#333"/></svg></span></div>
      <div class="price">$25.00</div><div class="add"><svg width="16" height="14" viewBox="0 0 16 14"><path d="M0 1h3l2 8h9l2-6H4.5" fill="none" stroke="#fff" stroke-width="2"/><circle cx="6" cy="12.5" r="1.5" fill="#fff"/><circle cx="13" cy="12.5" r="1.5" fill="#fff"/></svg>Add to Cart</div></div>
  </article>
  <article class="card">
    <div class="photo" role="img" aria-label="Volunteer in navy hoodie holding a mug beside a golden retriever" style="background:linear-gradient(135deg,#d8c8b0,#273a66 55%,#a88762)"></div>
    <div class="card-body"><h3>Bright Meadow Hoodie</h3><p>Cozy hoodie perfect for cool weather visits</p>
      <div class="size" style="margin-top:33px">Size: <span class="select">S <svg width="8" height="5"><path d="M0 0l4 5 4-5" fill="#333"/></svg></span></div>
      <div class="price">$45.00</div><div class="add"><svg width="16" height="14" viewBox="0 0 16 14"><path d="M0 1h3l2 8h9l2-6H4.5" fill="none" stroke="#fff" stroke-width="2"/><circle cx="6" cy="12.5" r="1.5" fill="#fff"/><circle cx="13" cy="12.5" r="1.5" fill="#fff"/></svg>Add to Cart</div></div>
  </article>
  <article class="card">
    <div class="photo" role="img" aria-label="Canvas tote bag with a golden retriever" style="background:linear-gradient(135deg,#c9a47a,#2f3f6b 55%,#e6d6bb)"></div>
    <div class="card-body"><h3>Bright Meadow Tote Bag</h3><p>Durable canvas tote for carrying treats and toys</p>
      <div class="price">$20.00</div><div class="add"><svg width="16" height="14" viewBox="0 0 16 14"><path d="M0 1h3l2 8h9l2-6H4.5" fill="none" stroke="#fff" stroke-width="2"/><circle cx="6" cy="12.5" r="1.5" fill="#fff"/><circle cx="13" cy="12.5" r="1.5" fill="#fff"/></svg>Add to Cart</div></div>
  </article>

  <article class="card">
    <div class="photo" role="img" aria-label="Volunteer holding a coffee mug beside a golden retriever" style="background:linear-gradient(135deg,#c9a47a,#2f3f6b 60%,#e8dcc6)"><span class="tag">New</span></div>
    <div class="card-body"><h3>Bright Meadow Coffee Mug</h3><p>Start your morning with puppy love</p>
      <div class="price">$15.00</div><div class="add"><svg width="16" height="14" viewBox="0 0 16 14"><path d="M0 1h3l2 8h9l2-6H4.5" fill="none" stroke="#fff" stroke-width="2"/><circle cx="6" cy="12.5" r="1.5" fill="#fff"/><circle cx="13" cy="12.5" r="1.5" fill="#fff"/></svg>Add to Cart</div></div>
  </article>
  <article class="card">
    <div class="photo" role="img" aria-label="Vinyl stickers on a wooden table" style="background:linear-gradient(135deg,#e8dcc6,#c99a63 50%,#2f3f6b)"></div>
    <div class="card-body"><h3>Bright Meadow Sticker Pack</h3><p>Set of 5 vinyl stickers, waterproof</p>
      <div class="price">$8.00</div><div class="add"><svg width="16" height="14" viewBox="0 0 16 14"><path d="M0 1h3l2 8h9l2-6H4.5" fill="none" stroke="#fff" stroke-width="2"/><circle cx="6" cy="12.5" r="1.5" fill="#fff"/><circle cx="13" cy="12.5" r="1.5" fill="#fff"/></svg>Add to Cart</div></div>
  </article>
  <article class="card">
    <div class="photo" role="img" aria-label="Navy baseball cap on a wooden table" style="background:linear-gradient(135deg,#e8dcc6,#2a3b66 50%,#c99a63)"></div>
    <div class="card-body"><h3>Bright Meadow Baseball Cap</h3><p>Adjustable cap with embroidered logo</p>
      <div class="price">$18.00</div><div class="add"><svg width="16" height="14" viewBox="0 0 16 14"><path d="M0 1h3l2 8h9l2-6H4.5" fill="none" stroke="#fff" stroke-width="2"/><circle cx="6" cy="12.5" r="1.5" fill="#fff"/><circle cx="13" cy="12.5" r="1.5" fill="#fff"/></svg>Add to Cart</div></div>
  </article>

  <article class="card">
    <div class="photo" role="img" aria-label="Navy water bottle and leash on a wooden table" style="background:linear-gradient(135deg,#e8dcc6,#243663 45%,#c99a63)"></div>
    <div class="card-body"><h3>Bright Meadow Water Bottle</h3><p>Stay hydrated during walks and visits</p>
      <div class="price">$22.00</div><div class="add"><svg width="16" height="14" viewBox="0 0 16 14"><path d="M0 1h3l2 8h9l2-6H4.5" fill="none" stroke="#fff" stroke-width="2"/><circle cx="6" cy="12.5" r="1.5" fill="#fff"/><circle cx="13" cy="12.5" r="1.5" fill="#fff"/></svg>Add to Cart</div></div>
  </article>
  <article class="card">
    <div class="photo" role="img" aria-label="Enamel pin on a display card on a wooden table" style="background:linear-gradient(135deg,#e8dcc6,#c99a63 55%,#243663)"></div>
    <div class="card-body"><h3>Bright Meadow Enamel Pin</h3><p>Collectible pin featuring Maple</p>
      <div class="price">$10.00</div><div class="add"><svg width="16" height="14" viewBox="0 0 16 14"><path d="M0 1h3l2 8h9l2-6H4.5" fill="none" stroke="#fff" stroke-width="2"/><circle cx="6" cy="12.5" r="1.5" fill="#fff"/><circle cx="13" cy="12.5" r="1.5" fill="#fff"/></svg>Add to Cart</div></div>
  </article>
  <article class="card">
    <div class="photo" role="img" aria-label="Navy dog bandana on a wooden table" style="background:linear-gradient(135deg,#e8dcc6,#243663 50%,#c99a63)"></div>
    <div class="card-body"><h3>Bright Meadow Bandana</h3><p>Collectible Bandana featuring Maple</p>
      <div class="price">$10.00</div><div class="add"><svg width="16" height="14" viewBox="0 0 16 14"><path d="M0 1h3l2 8h9l2-6H4.5" fill="none" stroke="#fff" stroke-width="2"/><circle cx="6" cy="12.5" r="1.5" fill="#fff"/><circle cx="13" cy="12.5" r="1.5" fill="#fff"/></svg>Add to Cart</div></div>
  </article>
</main>

<section class="cart-bar">
  <div class="cart-icon"><svg width="30" height="26" viewBox="0 0 16 14"><path d="M0 1h3l2 8h9l2-6H4.5z" fill="#1b3a4b" stroke="#1b3a4b" stroke-width="1.6" stroke-linejoin="round"/><circle cx="6" cy="12.5" r="1.5" fill="#1b3a4b"/><circle cx="13" cy="12.5" r="1.5" fill="#1b3a4b"/></svg><span class="cart-count">0</span></div>
  <span class="total">Total:</span><span class="total-amount">$0.00</span>
  <div class="checkout"><svg width="17" height="12" viewBox="0 0 17 12"><rect x="0.5" y="0.5" width="16" height="11" rx="2" fill="#fff"/><rect x="0.5" y="3" width="16" height="2.5" fill="#1b3a4b"/></svg>Checkout</div>
</section>

<section class="bulk">
  <h2>Want to Order in Bulk?</h2>
  <p>For team orders of 10+ items, contact us for special pricing.</p>
  <div class="contact"><svg width="16" height="12" viewBox="0 0 16 12"><rect width="16" height="12" rx="1.5" fill="#fff"/><path d="M1 1l7 5 7-5" fill="none" stroke="#d4896a" stroke-width="1.5"/></svg>Contact Us</div>
</section>

<footer class="site-footer">
  <div class="foot-brand">
    <div class="brand-name">Bright Meadow<br>Therapy Dogs</div>
    <p>Bringing comfort, joy and unconditional love — One Paw at a time.</p>
    <div class="foot-social"><span role="img" aria-label="Social media link"></span><span role="img" aria-label="Photo sharing link"></span></div>
  </div>
  <div class="foot-col" style="left:457px"><h4>Quick Links</h4><ul><li>Home</li><li>Our Team</li><li>Donors &amp; Referrals</li><li>Team Store</li></ul></div>
  <div class="foot-col" style="left:659px"><h4>Get Involved</h4><ul><li>Join Our Pack</li><li>Request a Visit</li><li>Donate</li></ul></div>
  <div class="foot-col" style="left:862px"><h4>Contact Us</h4><ul>
    <li><svg width="13" height="10" viewBox="0 0 16 12"><rect width="16" height="12" rx="1.5" fill="#d4896a"/><path d="M1 1l7 5 7-5" fill="none" stroke="#14283a" stroke-width="1.5"/></svg>info@brightmeadow.org</li>
    <li><svg width="13" height="13" viewBox="0 0 24 24"><path d="M6.6 10.8a15.1 15.1 0 006.6 6.6l2.2-2.2c.3-.3.7-.4 1-.2 1.1.4 2.3.6 3.6.6.6 0 1 .4 1 1V20c0 .6-.4 1-1 1A17 17 0 013 4c0-.6.4-1 1-1h3.5c.6 0 1 .4 1 1 0 1.3.2 2.5.6 3.6.1.3 0 .7-.2 1z" fill="#d4896a"/></svg>(555) 010-4821</li>
  </ul></div>
  <div class="copyright">© 2026 Bright Meadow Therapy Dogs. All rights reserved.</div>
</footer>
</body>
</html>
```